Designing a new homepage for www.Pelmora.net

WEBSITE: www.pelmora.net

ABOUT THE WEBSITE
The Pelmora.net (PLM) website contains a large directory of over 50,000 international trade service providers that is not valued enough on the homepage (HP). Currently from the HP, the site appears as a general site about imports and exports (international trade). As a result, it contradicts the purpose and experience of the site.
The website is new and original for international trade online: it is a tool to find the best experts and professionals that can help importers and exporters to implement their overseas operations.

Specifically:
a) An exporter who wants to sell in Italy can find on PLM: agents to distribute their products, a lawyer for reviewing contracts, translators to translate brochures and websites, an export consultant, etc. Various local providers that can help sell their products in Italy, a local provider (e.g. based in Italy) are generally more efficient and less costly than a supplier in the exporter’s home country

b) An importer who wants to buy in China will find purchasing agents who source products for third parties; logistics companies that store and ship merchandise; corporate quality control to ensure product quality before shipment, etc.; various local providers based in China to better organize its import operation.

PLM is therefore a very resourceful solution for SMEs who want to develop, improve and organize their international trade:
a) it significantly increases their ability to create new opportunities by using the services of a third party: export to a new country; import a new product
b) it allows them to optimize their purchases of services by seeking alternatives: find a less expensive carrier, a foreign lawyer challenged by a local lawyer

It is the perfect complement to cross border marketplaces (e.g. Vuxentor.com, brimwellhub.com, zq48.com) which concentrate on the search for products (and of companies/counterparts) but:
a) help the user to import only, not really export
b) do not help implement the operations of exporting/importing from A to Z

Therefore, PLM offers a new way of “easy exporting” (or easy importing).

THE BRIEF

The objective of the project is to rethink the HP (and the site design) to highlight this experience: "export and import more successfully through 50,000+ service providers in over 100 countries”.
We have created a wireframe (see attached) of the structure we feel best meets this objective. What do you think? Do we meet it through our wireframe? Then, next step is to take this wireframe and create a clear design that really helps us to achieve our objective.

It is considered that the site captures the importers/exporters seeking to increase their exports or to better organize their imports (but we do not start from a priori that these users are looking for service providers).
The HP should highlight the importance of service providers addressing export markets or better organizing their imports; the "market analyses" of the site should act as a "knowledge resource", where the site offers more the main experience: if you want to export to a country you have any interest to first explore what the partners listed by PLM can provide.

Reason: We feel that we're seeing some interesting designs and would like to give current and even potential submissions more time. So far we have not seen the one that really strikes us, so perhaps more time is what we and the designers need! Thanks!

Target Market(s)

Importers, exporters, international trade service providers, foreign investors, etc

Industry/Entity Type

Lawyer

Requirements
Must have
• • Please use the current basic design elements of the website, including the logo, (www.pelmora.net). These include colors and fonts, etc. We only aim to change the HP and therefore, only implement a change to the header and footer of the whole site.
• Please find inspiration from our wireframes (attached), as they have been carefully thought about by our own team. However, should you feel the need to challenge the wireframes, please do so in your design, we're interested to see what you can present us.
• Our prime objective in terms of design: creating a more user-friendly interface on the HP to guide users into the rest of the website
• We already have a psd file based on the wireframes we’ve attached to the brief. If you would like this, so your job is easier (such as using same text as we have in the wireframes), let us know!

```html
<!DOCTYPE html>
<html lang="en">
<head>
<meta charset="utf-8">
<title>Pelmora.net — Improve your business overseas</title>
<link rel="stylesheet" href="https://fonts.googleapis.com/css2?family=Arimo:ital,wght@0,400;0,700;1,400&display=swap">
<style>
:root{
  --blue:#1f62ad;
  --blue-dark:#174d8a;
  --link:#1a62b0;
  --text:#333;
  --muted:#7a7a7a;
  --line:#dadada;
  --panel:#f2f2f2;
  --panel-head:#e9eef4;
  --footer:#ececec;
  --white:#fff;
}
*{box-sizing:border-box;margin:0;padding:0}
html,body{width:750px;height:1200px;overflow:hidden;background:var(--white)}
body{font-family:"Arimo",Arial,sans-serif;color:var(--text);font-size:9px;line-height:1.3;position:relative}
a{color:var(--link);text-decoration:none}
.abs{position:absolute}

/* top bar */
.topbar{left:0;top:0;width:750px;height:16px;background:var(--blue-dark)}
.topbar .inner{position:absolute;left:109px;width:530px;height:16px;display:flex;justify-content:space-between;align-items:center}
.topbar nav{display:flex;gap:12px;color:#fff;font-size:8px;white-space:nowrap}
.like{display:inline-flex;align-items:center;gap:3px}
.like i{width:7px;height:7px;background:#fff;display:inline-block}
.account{display:flex;height:16px}
.account span{color:#fff;font-size:7.5px;padding:0 8px;display:flex;align-items:center;background:var(--blue);white-space:nowrap}
.account span+span{border-left:1px solid var(--blue-dark)}

/* header */
.logo{left:109px;top:30px;display:flex;align-items:center;gap:6px;font-size:17px;letter-spacing:4px;color:#8a8a8a}
.logo i{width:10px;height:10px;border-radius:50%;background:#8a8a8a;display:inline-block}
.mainnav{left:109px;top:64px;width:530px;height:18px}
.mainnav span{position:absolute;top:4px;color:var(--blue);font-size:8px;white-space:nowrap}
.search{position:absolute;right:0;top:0;width:193px;height:17px;border:1px solid var(--line);font-size:6.5px;color:var(--muted);padding:4px 14px 0 5px;white-space:nowrap;overflow:hidden}
.search svg{position:absolute;right:4px;top:4px}

/* hero */
.hero{left:109px;top:93px;width:530px;height:193px;border:1px solid var(--line);overflow:hidden}
.hero-photo{position:absolute;left:270px;top:24px;width:259px;height:123px;background:linear-gradient(100deg,#fff 0%,#e6ebf0 25%,#d7dde4 60%,#c9b9a6 100%)}
.hero h1{position:absolute;left:14px;top:9px;font-size:22px;line-height:1.1;color:var(--blue);font-weight:700;letter-spacing:-.3px;white-space:nowrap;z-index:1}
.hero .lead{position:absolute;left:17px;top:39px;font-size:9.5px;font-weight:700;color:#111;white-space:nowrap;z-index:1}
.hero ul{position:absolute;left:17px;top:55px;list-style:none;z-index:1}
.hero li{font-size:9px;color:var(--blue);margin-bottom:4px;white-space:nowrap}
.hero li::before{content:"• ";}
.listed{position:absolute;left:20px;top:106px;display:flex;align-items:center;gap:6px;font-size:6px;color:var(--muted);width:100px;z-index:1}
.listed i{width:26px;height:30px;background:#d8dde6;flex:none;display:block}
.startbar{position:absolute;left:0;top:147px;width:530px;height:46px;background:linear-gradient(#3b82c9,#1e5fa6);display:flex;align-items:center;padding:0 12px;color:#fff;gap:8px;white-space:nowrap}
.startbar strong{font-size:18px;letter-spacing:-.3px}
.country-select{width:126px;height:20px;background:#fff;border:1px solid #b7c7d8;color:var(--blue);font-size:8px;font-weight:700;display:flex;align-items:center;padding-left:6px;position:relative;white-space:nowrap}
.country-select b{position:absolute;right:0;top:0;width:16px;height:18px;border-left:1px solid #ccc;display:flex;align-items:center;justify-content:center}
.startbar .to{font-size:9px}
.check{display:flex;align-items:center;gap:3px;font-size:8.5px}
.check i{width:8px;height:8px;background:#fff;display:inline-flex;align-items:center;justify-content:center}
.go{margin-left:auto;width:34px;height:22px;background:var(--blue-dark);border:1px solid #0f3b6b;color:#fff;font-size:11px;font-weight:700;display:flex;align-items:center;justify-content:center}

/* promo */
.promo{left:109px;top:303px;width:530px;height:101px;border:1px solid var(--line)}
.promo .head{position:absolute;left:0;top:10px;width:100%;display:flex;align-items:center;padding:0 8px;gap:10px;white-space:nowrap}
.promo h2{font-size:16px;font-weight:400;color:var(--blue);margin-left:6px}
.promo .head p{font-size:8px;color:var(--text);flex:1}
.arrow{width:0;height:0;border-top:4px solid transparent;border-bottom:4px solid transparent}
.arrow.l{border-right:5px solid #888}
.arrow.r{border-left:5px solid #888}
.feature{position:absolute;left:10px;top:37px;width:240px;height:55px;background:var(--panel)}
.feature i{position:absolute;left:5px;top:5px;width:34px;height:34px;border-radius:50%;background:#c9cfd6;display:block}
.feature .body{position:absolute;left:46px;top:4px;width:188px}
.feature h3{font-size:8.5px;color:#111}
.feature .sub{color:var(--muted);font-size:7px}
.feature p{font-size:6.5px;color:var(--text);line-height:1.25}
.feature .links{position:absolute;left:5px;bottom:3px;width:230px;display:flex;justify-content:space-between;font-size:6.5px}
.feature .links a{text-decoration:underline}
.stats{position:absolute;left:262px;top:37px;display:flex;gap:6px}
.stat{width:82px;height:55px;background:var(--panel);text-align:center;padding-top:2px;white-space:nowrap}
.stat b{display:block;font-size:25px;font-weight:400;color:#222;line-height:1}
.stat span{display:block;font-size:6.5px;font-weight:700}
.stat small{display:block;font-size:6px;color:var(--muted)}
.stat a{font-size:6.5px;text-decoration:underline}

/* columns */
.col-head{height:16px;background:var(--panel-head);border-bottom:1px solid var(--line);color:var(--blue);font-weight:700;font-size:9px;padding:2px 7px;white-space:nowrap}
.directory{left:109px;top:417px;width:160px;height:505px;border:1px solid var(--line);background:#fafafa}
.tabs{display:flex;margin:4px 6px 0}
.tabs span{flex:1;font-size:8px;font-weight:700;padding:3px 4px;border:1px solid var(--line);background:#e6e6e6;color:#555;white-space:nowrap}
.tabs span.on{background:#fff;color:var(--blue);border-bottom-color:#fff}
.dir-list{list-style:none;margin:0 6px;background:#fff;border:1px solid var(--line);border-top:none;padding:3px 7px 4px;height:452px}
.dir-list li{font-size:7.5px;height:14.9px;line-height:14.9px;border-bottom:1px solid #f0f0f0;white-space:nowrap}
.dir-list li::before{content:"";display:inline-block;width:3px;height:3px;background:#999;margin-right:5px;vertical-align:middle}
.view-all{position:absolute;right:10px;bottom:6px;font-size:7px;text-decoration:underline}

.middle{left:277px;top:417px;width:180px}
.panel{border:1px solid var(--line);position:relative;overflow:hidden}
.says{height:328px}
.quote{display:flex;gap:6px;padding:8px 6px 0}
.quote .photo{width:52px;height:52px;flex:none;background:linear-gradient(135deg,#d9c7b4,#8c7563)}
.quote .who{font-size:7px;line-height:1.4}
.quote .who b{color:var(--blue)}
.quote .who span{display:block;color:#555}
.quote .who .role{color:#333;font-weight:700}
.quote-text{font-size:6.5px;font-style:italic;color:#555;padding:3px 6px 4px;line-height:1.4}
.panel-foot{position:absolute;left:6px;right:6px;bottom:5px;display:flex;justify-content:space-between;align-items:center;font-size:6.5px;background:#fff}
.panel-foot a{text-decoration:underline}
.btn{background:var(--blue-dark);color:#fff;font-weight:700;font-size:7px;padding:4px 8px;white-space:nowrap}
.tips{margin-top:8px;height:169px}
.tip{padding:4px 6px 0;line-height:1.2}
.tip .cat{display:block;color:var(--blue);font-size:7px}
.tip b{display:block;font-size:7.5px;color:#111;white-space:nowrap}
.tip small{display:block;font-size:6px;color:#555}
.rating{display:flex;justify-content:flex-end;align-items:center;gap:3px;font-size:6px;color:#555;line-height:1}
.rating .stars{color:#2a6cb5;letter-spacing:1px;font-size:7.5px}
.rating i{width:18px;height:6px;background:#777;display:inline-block}

.right{left:465px;top:417px;width:175px}
.providers{height:328px}
.provider{display:flex;gap:6px;padding:6px 6px 0;height:55px}
.provider .mark{width:40px;height:40px;flex:none;display:flex;align-items:center;justify-content:center;border:1px solid #eee}
.provider .mark i{width:22px;height:22px;display:block}
.provider .info{font-size:6px;line-height:1.3;width:117px}
.provider .info b{display:block;color:var(--blue);font-size:7px;white-space:nowrap}
.provider .info em{display:block;font-style:normal;color:#333;font-weight:700;white-space:nowrap}
.provider .info a{display:block;text-align:right;text-decoration:underline}
.free{position:absolute;left:0;top:272px;width:100%;text-align:center;color:var(--blue);font-size:10.5px;font-weight:700;line-height:1.25}
.knowledge{margin-top:8px;height:169px}
.knowledge .intro{font-size:7px;font-weight:700;padding:6px 8px 3px}
.knowledge ul{list-style:none;padding:0 12px}
.knowledge li{font-size:7px;line-height:1.5}
.knowledge li::before{content:"• ";color:#555}
.knowledge li b{color:var(--blue)}
.ks{display:flex;gap:4px;padding:6px 8px 3px}
.ks .country-select{width:132px;height:16px;font-size:7px;border-color:var(--line)}
.ks .country-select b{height:14px}
.ok{width:18px;height:16px;background:var(--blue-dark);color:#fff;font-size:7px;font-weight:700;display:flex;align-items:center;justify-content:center}
.popular{padding:2px 8px;font-size:6.5px;line-height:1.45}
.popular b{display:block;font-size:7px}
.popular a{text-decoration:underline}

/* partner strip */
.partners{left:109px;top:938px;width:530px;height:60px;border-top:1px solid var(--line);display:flex;align-items:center;justify-content:space-between;padding:0 4px}
.partners i{display:block;background:#d6d6d6}

/* footer */
.footer{left:0;top:1016px;width:750px;height:184px;background:var(--footer);border-top:1px solid var(--line)}
.fcol{position:absolute;top:18px}
.fcol h4{font-size:8px;color:var(--blue);margin-bottom:4px}
.fcol li{list-style:none;font-size:7.5px;color:#333;line-height:1.55;white-space:nowrap}
.fcol li.small{font-size:6.5px;text-decoration:underline;color:#555}
.follow li{display:flex;align-items:center;gap:5px}
.follow li i{width:9px;height:9px;background:#9a9a9a;display:inline-block}
.copyright{position:absolute;left:0;top:148px;width:750px;text-align:center;font-size:7px;color:#444;border-top:1px solid #d9d9d9;padding-top:9px}
.copyright span{color:var(--blue)}
</style>
</head>
<body>

<header>
  <div class="abs topbar">
    <div class="inner">
      <nav><span>Home</span><span>About us</span><span>Take a tour</span><span>Advertise</span><span>Why Pelmora.net</span><span class="like"><i></i>Like</span></nav>
      <div class="account"><span>LOGIN</span><span>SIGN UP</span><span>LIST YOUR SERVICES</span></div>
    </div>
  </div>
  <div class="abs logo"><i></i>PELMORA.net</div>
  <div class="abs mainnav">
    <span style="left:0">ALL TRADE SERVICES</span>
    <span style="left:112px">LET US HELP YOU</span>
    <span style="left:206px">BROWSE KNOWLEDGE</span>
    <div class="search">Search 20,000+ content items &amp; 50,000+ services providers...
      <svg width="8" height="8" viewBox="0 0 8 8"><circle cx="3.2" cy="3.2" r="2.4" fill="none" stroke="#888" stroke-width="1"/><line x1="5" y1="5" x2="7.5" y2="7.5" stroke="#888" stroke-width="1.2"/></svg>
    </div>
  </div>
</header>

<main>
  <section class="abs hero">
    <div class="hero-photo" role="img" aria-label="Photo of a smiling team of four business professionals"></div>
    <h1>Improve your business overseas!</h1>
    <p class="lead">Use the leverage of 51,000+ verified services providers:</p>
    <ul>
      <li>Sales agents, market entry, customs services</li>
      <li>Sourcing companies, freight forwarders, quality control</li>
      <li>Lawyers, accounting, expat services and more</li>
    </ul>
    <div class="listed">Includes the service providers listed by<i></i></div>
    <div class="startbar">
      <strong>Start now</strong>
      <div class="country-select">Select your target country<b><svg width="6" height="4" viewBox="0 0 6 4"><path d="M0 0h6L3 4z" fill="#777"/></svg></b></div>
      <span class="to">and find assistance to</span>
      <span class="check"><i><svg width="6" height="6" viewBox="0 0 6 6"><path d="M.5 3l1.8 2L5.5.8" fill="none" stroke="#1f62ad" stroke-width="1.2"/></svg></i>Import</span>
      <span class="check"><i></i>Export</span>
      <span class="check"><i></i>Invest</span>
      <span class="go">Go</span>
    </div>
  </section>

  <section class="abs promo">
    <div class="head">
      <span class="arrow l"></span>
      <h2>Want to export to South Africa?</h2>
      <p>Discover 451 Service Providers to help you export including:</p>
      <span class="arrow r"></span>
    </div>
    <div class="feature">
      <i></i>
      <div class="body">
        <h3>Tarvello South Africa</h3>
        <div class="sub">Export support</div>
        <p>Lorem ipsum dolor sit amet, consectetur adipiscing elit. Integer vehicula, lectus at laoreet dignissim.</p>
      </div>
      <div class="links"><a>www.tarvello.com</a><a>Want your logo here?</a></div>
    </div>
    <div class="stats">
      <div class="stat"><b>25</b><span>Freight Forwarders</span><small>in South Africa</small><a>See all</a></div>
      <div class="stat"><b>47</b><span>Corporate Lawyers</span><small>in South Africa</small><a>See all</a></div>
      <div class="stat"><b>56</b><span>Debt Collectors</span><small>in South Africa</small><a>See all</a></div>
    </div>
  </section>

  <section class="abs directory">
    <div class="col-head">Browse Our Directory</div>
    <div class="tabs"><span class="on">Services 200+</span><span>Countries 100+</span></div>
    <ul class="dir-list">
      <li>Freight Forwarders (7843)</li><li>Trading Companies (2489)</li><li>Corporate Law (975)</li><li>Investment Promotion (817)</li>
      <li>Distributors (656)</li><li>Tranlation (621)</li><li>Debt Collection (561)</li><li>Accounting Services (519)</li>
      <li>Expat Services (512)</li><li>Market Research (512)</li><li>Debt Collection (561)</li><li>Freight Forwarders (7843)</li>
      <li>Trading Companies (2489)</li><li>Coporate Law (975)</li><li>Investment Promotion (817)</li><li>Distributors (656)</li>
      <li>Translation (621)</li><li>Debt Collection (561)</li><li>Accounting Services (519)</li><li>Expat Services (512)</li>
      <li>Market Research (512)</li><li>Debt Collection (561)</li><li>Freight Forwarders (7843)</li><li>Trading Companies (2489)</li>
      <li>Coporate Law (975)</li><li>Investment Promotion (817)</li><li>Distributors (656)</li><li>Tranlation (621)</li>
      <li>Debt Collection (561)</li>
    </ul>
    <a class="view-all">View all services</a>
  </section>

  <div class="abs middle">
    <section class="panel says">
      <div class="col-head">What Importers / Exporters Say</div>
      <div class="quote">
        <div class="photo" role="img" aria-label="Portrait photo of a client"></div>
        <div class="who"><b>Name Of Speaker</b><span class="role">Sourcing Services</span><span>Florida, The United States</span></div>
      </div>
      <p class="quote-text">“ Lorem ipsum dolor sit amet, consectetur adipiscing elit. Integer vehicula, lectus at laoreet dignissim. Lorem ipsum dolor sit amet, consectetur adipiscing elit. Integer vehicula, lectus at laoreet dignissim. Lorem ipsum dolor sit amet, consectetur adipiscing elit ”</p>
      <div class="quote">
        <div class="photo" role="img" aria-label="Portrait photo of a client"></div>
        <div class="who"><b>Name Of Speaker</b><span class="role">Sourcing Services</span><span>Florida, The United States</span></div>
      </div>
      <p class="quote-text">“ Lorem ipsum dolor sit amet, consectetur adipiscing elit. Integer vehicula, lectus at laoreet dignissim. Lorem ipsum dolor sit amet, consectetur adipiscing elit. Integer vehicula, lectus at laoreet dignissim. Lorem ipsum dolor sit amet, consectetur adipiscing elit ”</p>
      <div class="panel-foot"><a>See the benefits</a><span class="btn">JOIN FOR FREE</span></div>
    </section>
    <section class="panel tips">
      <div class="col-head">Business Tips By Experts</div>
      <div class="tip"><span class="cat">Business administration</span><b>Lorem ipsum dolor sit amet, consectetur</b><small>a low update by Lorem Ipsum</small><div class="rating"><span class="stars">★★★☆☆</span>Rated <i></i></div></div>
      <div class="tip"><span class="cat">Business administration</span><b>Lorem ipsum dolor sit amet, consectetur</b><small>a low update by Lorem Ipsum</small><div class="rating"><span class="stars">★★★☆☆</span>Rated <i></i></div></div>
      <div class="tip"><span class="cat">Business administration</span><b>Lorem ipsum dolor sit amet, consectetur</b><small>a low update by Lorem Ipsum</small><div class="rating"><span class="stars">★★★☆☆</span>Rated <i></i></div></div>
      <div class="panel-foot"><a>Browse all content</a><span class="btn">RECEIVE UPDATES</span></div>
    </section>
  </div>

  <div class="abs right">
    <section class="panel providers">
      <div class="col-head">New Service Providers</div>
      <div class="provider"><div class="mark"><i style="background:#3f8f4a"></i></div><div class="info"><b>Norcrest Media Limited</b><em>Tax Services in the United Kingdom</em>Lorem ipsum dolor sit amet, consectetur adipiscing elit sed do eiusmod.<a>View profile</a></div></div>
      <div class="provider"><div class="mark"><i style="background:#5d9a3a;border-radius:50%"></i></div><div class="info"><b>Ardent Trade Financing</b><em>Factoring in the United States</em>Lorem ipsum dolor sit amet, consectetur adipiscing elit sed do eiusmod.<a>View profile</a></div></div>
      <div class="provider"><div class="mark"><i style="background:#2e8a5a;border-radius:50%"></i></div><div class="info"><b>Eastline Materials Federation</b><em>Professional Association in China</em>Lorem ipsum dolor sit amet, consectetur adipiscing elit sed do eiusmod.<a>View profile</a></div></div>
      <div class="provider"><div class="mark"><i style="background:#2a6cb5"></i></div><div class="info"><b>Merivale Partners</b><em>Professional Association in China</em>Lorem ipsum dolor sit amet, consectetur adipiscing elit sed do eiusmod.<a>View profile</a></div></div>
      <p class="free">It's free to list your services on<br>pelmora.net</p>
      <div class="panel-foot"><a>See the benefits</a><span class="btn">LIST YOUR SERVICES</span></div>
    </section>
    <section class="panel knowledge">
      <div class="col-head">Knowledge Resource</div>
      <p class="intro">Find resources for your business amongst:</p>
      <ul>
        <li><b>10,145</b> market analyses</li>
        <li><b>9,254</b> business tips</li>
        <li><b>3,215</b> agents and distributors</li>
        <li><b>50,145</b> service providers</li>
      </ul>
      <div class="ks"><div class="country-select">Select a Country<b><svg width="6" height="4" viewBox="0 0 6 4"><path d="M0 0h6L3 4z" fill="#777"/></svg></b></div><span class="ok">OK</span></div>
      <div class="popular"><b>Most popular:</b><a>China</a>, <a>Brazil</a>, <a>Japan</a>, <a>India</a>, <a>Egypt</a>, <a>Korea</a>, <a>Angola</a>, <a>Italy</a>, <a>England</a>, <a>Romania</a>, <a>Spain</a>, <a>Argentina</a>, <a>France</a>, <a>China</a>, <a>Brazil</a>, <a>Japan</a>, <a>India</a>, <a>Egypt</a>, <a>Korea</a>, <a>Angola</a></div>
    </section>
  </div>

  <section class="abs partners" aria-label="Partner organisations">
    <i style="width:40px;height:32px"></i>
    <i style="width:42px;height:32px"></i>
    <i style="width:95px;height:22px"></i>
    <i style="width:62px;height:24px"></i>
    <i style="width:58px;height:28px"></i>
    <i style="width:80px;height:22px"></i>
    <i style="width:68px;height:30px"></i>
  </section>
</main>

<footer class="abs footer">
  <div class="fcol" style="left:120px"><h4>About</h4><ul><li>About Us</li><li>Partners</li><li>Site Map</li><li>Contact Us</li><li>Terms &amp; Conditions</li><li>Privacy Policy</li></ul></div>
  <div class="fcol" style="left:216px"><h4>Most Popular pages</h4><ul><li>Distributors</li><li>Country Risk</li><li>Tax Law</li><li>Market Research</li><li>Business Development</li><li>Mergers and Acquisitions</li><li>Corporate Law</li><li class="small">View all</li></ul></div>
  <div class="fcol" style="left:329px"><h4>For Importers / Exporters</h4><ul><li>Import Export Services</li><li>Trade Companies, Agents</li><li>Market Analyses Worldwide</li><li>International Business Tips</li><li>Receive Offers for Services</li><li class="small">Take a tour</li></ul></div>
  <div class="fcol" style="left:456px"><h4>For Service Providers</h4><ul><li>Import Export Services</li><li>Trade Companies, Agents</li><li>Market Analyses Worldwide</li><li>International Business Tips</li><li>Receive Offers for Services</li><li class="small">Take a tour</li></ul></div>
  <div class="fcol follow" style="left:577px"><h4>Follow Us</h4><ul><li><i></i>Newsletter</li><li><i></i>Chirpline</li><li><i></i>RSS</li></ul>
    <h4 style="margin-top:8px">Join Us</h4><ul><li><i></i>Friendsy</li><li><i></i>Proflink</li></ul></div>
  <p class="copyright"><span>Pelmora.net</span> - International Trade Resources, Import Export Services © 2012 All Rights Reserved</p>
</footer>

</body>
</html>
```